■依頼の目的/概要
弊社が販売している化粧品『Kavro(カーヴロ)』のラベルデザインをお願いします。
・化粧水『ピュアラローション』
・乳液『ピュアラミルク』
・美容液

■依頼詳細
・シリーズでの販売となるため、統一されたデザインでお願いします。
ロゴはデザインに合うものに換えて頂いてもかまいません。
※現在のロゴは添付ファイルをご確認ください。

・化粧品・乳液のシールのサイズは、高さ10mm×幅5mm四方に収まるくらいでお願いします。※形状は変形してもOKです。(円型もOK)

・美容液のシールサイズは、高さ45㎜×幅30四方に収まるくらいでお願いします。※形状は変形してもOKです。(円型もOK)

■化粧品のコンセプト
お肌のトラブルの原因・乾燥を改善するために開発したシリーズで
植物は本来の保湿力と刺激の少ない高保湿成分を配合し保湿を重視した化粧品
・特徴
1お肌のトラブルの原因・乾燥を改善するために開発したシリーズ。
2 普通肌〜乾燥肌まで対応。乾燥からくる敏感肌の方にも。
3 無香料・ノンアルコールの安全設計。
4 保湿成分が高配合。長時間うるおいをしっかりキープします。
5 年齢とともに乾燥しやすい方、お手入れをしても乾きやすい方に。
6 バリア機能を強化し、乾きにくくダメージに強いお肌に整えます。

■デザインについて
イメージに合うデザインを添付致しましたので、ご参照ください。

*容器につきましては
化粧水 200ml 高さ180mm
乳液  120ml 高さ170mm
美容液 30ml
化粧水・乳液の容器については添付ファイルをご確認下さい。

その他何かご不明な点がございましたら、お気軽にご質問下さい。
よろしくお願いいたします。

◆納品の形式について
データの形式はイラストレータ(.ai)、pngでお願い致します。

◆選択させて頂いたデザインの著作権(財産権)等の扱いはTorvexa利用規約に従い、弊社に譲渡をお願いします。フォントや画像素材などを利用する場合は上記利用用途に使用できることを確認し、第三者の知的財産権等に注意して下さい。

美容液のボトルのイメージ画像を添付させて頂きます。
ラベルの幅と高さの指定が1桁ずれておりました。
申し訳ございません。

幅100mm、高さ50mmでの作成をお願いいたします。

ナチュラルイメージ、かつシンプルなデザインが気に入りました。

この度はコンペへご参加いただきありがとうございました。
今後ともどうぞよろしくお願い申し上げます!

```html
<!DOCTYPE html>
<html lang="ja">
<head>
<meta charset="utf-8">
<title>Kavro Pura Lotion Label</title>
<link rel="stylesheet" href="https://fonts.googleapis.com/css2?family=Cormorant+Garamond:wght@500;600&display=swap">
<style>
  :root {
    --paper: #ffffff;
    --trim: #555555;
    --ink: #7d6a5e;
    --frame: #8f7f75;
    --pink: #f6b6b9;
    --peach: #f7cfb8;
    --lemon: #f6f1b2;
    --mint: #d3f1d6;
    --aqua: #ade8ee;
    --ornament: #b9aaa0;
  }
  html, body {
    margin: 0;
    padding: 0;
    width: 730px;
    height: 1200px;
    overflow: hidden;
    background: var(--paper);
  }
  .canvas {
    position: relative;
    width: 730px;
    height: 1200px;
  }
  .trim-marks {
    position: absolute;
    inset: 0;
  }
  .trim-marks line {
    stroke: var(--trim);
    stroke-width: 1.4;
  }
  .label {
    position: absolute;
    left: 122px;
    top: 122px;
    width: 482px;
    height: 956px;
    background: linear-gradient(to bottom,
      var(--pink) 0%,
      var(--peach) 22%,
      var(--lemon) 36%,
      var(--mint) 46%,
      var(--aqua) 62%,
      var(--paper) 100%);
  }
  .emblem {
    position: absolute;
    left: 76px;
    top: 80px;
    width: 330px;
    height: 560px;
  }
  .emblem svg { position: absolute; inset: 0; }
  .ornament {
    position: absolute;
    left: 95px;
    width: 140px;
    height: 46px;
    border-radius: 23px;
    background: var(--ornament);
    opacity: 0.55;
  }
  .ornament--top { top: 72px; }
  .ornament--bottom { bottom: 72px; }
  .brand-name {
    position: absolute;
    left: 0;
    right: 0;
    top: 205px;
    margin: 0;
    text-align: center;
    font-family: "Cormorant Garamond", serif;
    font-weight: 600;
    font-size: 98px;
    line-height: 1;
    color: var(--ink);
  }
  .product-name {
    position: absolute;
    left: 0;
    right: 0;
    top: 322px;
    margin: 0;
    text-align: center;
    font-family: "Cormorant Garamond", serif;
    font-weight: 500;
    font-size: 27px;
    letter-spacing: 1px;
    color: var(--ink);
  }
  .volume {
    position: absolute;
    left: 0;
    right: 0;
    top: 778px;
    margin: 0;
    text-align: center;
    font-family: "Cormorant Garamond", serif;
    font-weight: 500;
    font-size: 40px;
    color: var(--ink);
  }
</style>
</head>
<body>
<div class="canvas">
  <svg class="trim-marks" width="730" height="1200" viewBox="0 0 730 1200" aria-hidden="true">
    <!-- corners -->
    <line x1="0" y1="100" x2="100" y2="100"/><line x1="0" y1="122" x2="100" y2="122"/>
    <line x1="100" y1="0" x2="100" y2="100"/><line x1="122" y1="0" x2="122" y2="100"/>
    <line x1="630" y1="100" x2="730" y2="100"/><line x1="630" y1="122" x2="730" y2="122"/>
    <line x1="630" y1="0" x2="630" y2="100"/><line x1="604" y1="0" x2="604" y2="100"/>
    <line x1="0" y1="1100" x2="100" y2="1100"/><line x1="0" y1="1078" x2="100" y2="1078"/>
    <line x1="100" y1="1100" x2="100" y2="1200"/><line x1="122" y1="1100" x2="122" y2="1200"/>
    <line x1="630" y1="1100" x2="730" y2="1100"/><line x1="630" y1="1078" x2="730" y2="1078"/>
    <line x1="630" y1="1100" x2="630" y2="1200"/><line x1="604" y1="1100" x2="604" y2="1200"/>
    <!-- centre marks -->
    <line x1="245" y1="62" x2="485" y2="62"/><line x1="365" y1="0" x2="365" y2="100"/>
    <line x1="245" y1="1138" x2="485" y2="1138"/><line x1="365" y1="1100" x2="365" y2="1200"/>
    <line x1="0" y1="600" x2="100" y2="600"/><line x1="62" y1="480" x2="62" y2="720"/>
    <line x1="630" y1="600" x2="730" y2="600"/><line x1="668" y1="480" x2="668" y2="720"/>
  </svg>

  <div class="label">
    <div class="emblem">
      <svg width="330" height="560" viewBox="0 0 330 560" aria-hidden="true">
        <ellipse cx="165" cy="280" rx="160" ry="275" fill="var(--paper)" stroke="var(--frame)" stroke-width="9"/>
        <ellipse cx="165" cy="280" rx="146" ry="261" fill="none" stroke="var(--frame)" stroke-width="1.5"/>
      </svg>
      <div class="ornament ornament--top" role="img" aria-label="Floral scroll ornament above the brand name"></div>
      <h1 class="brand-name">Kavro</h1>
      <p class="product-name">Pura Lotion</p>
      <div class="ornament ornament--bottom" role="img" aria-label="Floral scroll ornament below the product name"></div>
    </div>
    <p class="volume">200ml</p>
  </div>
</div>
</body>
</html>
```